Long term design collaboration - mobile app design & web app design

We are looking for a talented mobile designer to help us improve our UI & UX for mobile app and web app.

The screens that need to be redesigned are attached.

There is potentially a lot more work in future design available for the successful candidate.
The successful candidate would have to take part in daily stand-up around 3 times per week.
The successful candidate would join a dev team
We are software company that does property management

```html
<!DOCTYPE html>
<html lang="en">
<head>
<meta charset="utf-8">
<title>Development Overview – Property App Screens</title>
<link href="https://fonts.googleapis.com/css2?family=Poppins:wght@400;500;600;700&display=swap" rel="stylesheet">
<style>
:root{
  --navy:#1d4e6e;
  --ink:#163f5a;
  --teal:#b2dfdc;
  --teal-deep:#a6d8d4;
  --sky:#eef8fc;
  --panel:#ffffff;
  --muted:#7d8b93;
  --orange:#f07a1c;
  --alert:#e0393b;
  --hint:#f2b21b;
  --page:#ffffff;
}
*{box-sizing:border-box;margin:0;padding:0}
html,body{width:1200px;height:1000px;overflow:hidden;background:var(--page)}
body{font-family:'Poppins',sans-serif;color:var(--ink)}
.board{position:absolute;left:0;top:0;width:2100px;height:1760px;transform:scale(.5682);transform-origin:0 0}
.phone{position:absolute;width:333px;height:727px;background:var(--sky);box-shadow:0 22px 40px rgba(20,50,70,.18)}
.phone > *{position:absolute}
.back{left:18px;top:40px;width:20px;height:28px}
.title{left:56px;top:36px;font-size:22px;font-weight:500;color:var(--navy);white-space:nowrap}
.tabs{left:7px;top:86px;height:21px;display:flex;gap:2px}
.tab{height:21px;line-height:21px;font-size:9px;color:var(--navy);background:var(--teal);padding:0 7px;border-radius:3px 3px 0 0;white-space:nowrap;position:relative}
.tab.active{background:var(--panel)}
.tab .dot{position:absolute;right:2px;top:2px;width:6px;height:6px;border-radius:50%;border:1px solid var(--alert)}
.tab .dot.ok{border-color:#4caf50}
.card{left:7px;top:107px;width:319px;height:531px;background:var(--panel)}
.card.plain{top:85px;height:553px}
.label{left:34px;font-size:16px;font-weight:500;color:var(--navy);display:flex;align-items:center;gap:6px}
.flag{width:13px;height:13px;border-radius:50%;font-size:9px;line-height:11px;text-align:center;font-weight:600}
.flag.alert{border:1.3px solid var(--alert);color:var(--alert)}
.flag.hint{border:1.3px solid var(--hint);color:var(--hint)}
.field{left:28px;width:277px;height:42px;background:var(--panel);box-shadow:0 1px 6px rgba(0,0,0,.12);border-radius:2px;display:flex;align-items:center;padding:0 40px 0 24px;font-size:14px;color:var(--ink)}
.field.soft{color:var(--muted)}
.field.tall{height:62px;line-height:1.25}
.field svg{position:absolute;right:14px;top:50%;margin-top:-10px}
.btn{left:21px;top:569px;width:291px;height:54px;background:var(--teal);color:var(--navy);font-size:21px;font-weight:500;text-align:center;line-height:54px;box-shadow:0 2px 5px rgba(0,0,0,.12)}
.nav{left:21px;top:654px;display:flex;gap:21px}
.nav-item{width:57px;height:57px;border-radius:6px;background:var(--panel);display:flex;flex-direction:column;align-items:center;justify-content:center;color:var(--navy);font-size:7px;gap:2px}
.nav-item.active{background:var(--navy);color:#fff}
.nav-item svg{width:34px;height:34px;stroke:currentColor;fill:none;stroke-width:1.6}
.notes{left:30px;top:148px;width:276px;height:84px;background:var(--panel);box-shadow:0 1px 6px rgba(0,0,0,.12);padding:14px 16px;font-size:13px;color:var(--ink)}
.notes span{color:#d4dde2;margin-left:20px}
.links{left:30px;width:276px;text-align:center;font-size:14px;color:var(--navy);word-spacing:8px}
.links a{color:var(--navy);text-decoration:underline;word-spacing:0;margin:0 4px}
.center-label{left:0;width:333px;text-align:center;font-size:16px;font-weight:500;color:var(--navy)}
.choice{top:176px;width:110px;height:42px;background:var(--panel);box-shadow:0 1px 6px rgba(0,0,0,.12);text-align:center;line-height:42px;font-size:14px}
.money{left:28px;width:277px;height:97px;background:var(--panel);box-shadow:0 1px 6px rgba(0,0,0,.14);text-align:center;padding-top:6px}
.money.pay{background:var(--teal);color:var(--navy)}
.money b{display:block;font-size:34px;font-weight:700;color:#111;line-height:44px}
.money.pay b{color:var(--navy);margin-top:8px}
.money small{display:block;font-size:14px;line-height:18px}
.money svg{position:absolute;right:14px;top:60px}
.option{left:28px;width:277px;height:42px;background:var(--panel);box-shadow:0 1px 6px rgba(0,0,0,.12);font-size:14px;padding:0 60px 0 22px;display:flex;align-items:center;line-height:1.25}
.option svg{position:absolute;right:10px;top:50%;margin-top:-14px}
</style>
</head>
<body>
<svg width="0" height="0" style="position:absolute">
  <defs>
    <symbol id="chev" viewBox="0 0 20 20"><polyline points="6,2 14,10 6,18" fill="none" stroke="#f07a1c" stroke-width="2.4" stroke-linecap="round" stroke-linejoin="round"/></symbol>
    <symbol id="backarrow" viewBox="0 0 20 28"><polyline points="15,3 5,14 15,25" fill="none" stroke="#1d4e6e" stroke-width="2.8" stroke-linecap="round" stroke-linejoin="round"/></symbol>
    <symbol id="i-home" viewBox="0 0 34 34"><path d="M3 16 L17 4 L31 16 M7 13 V30 H27 V13 M13 30 V20 H21 V30"/></symbol>
    <symbol id="i-overview" viewBox="0 0 34 34"><path d="M3 15 L16 4 L29 15 M7 12 V29 H22 M25 20 V12"/><circle cx="17" cy="19" r="6"/><path d="M21 23 L28 30"/></symbol>
    <symbol id="i-fin" viewBox="0 0 34 34"><ellipse cx="12" cy="6" rx="8" ry="3"/><path d="M4 6 V24 C4 27 20 27 20 24 V6 M4 12 C4 15 20 15 20 12 M4 18 C4 21 20 21 20 18"/><circle cx="25" cy="24" r="7"/><path d="M27 20.5 C26 19.5 22.5 19.8 23 22 C23.5 24 27.5 23.5 27.4 26 C27 28 24 28 22.8 27 M25 18.5 V29.5"/></symbol>
    <symbol id="i-msg" viewBox="0 0 34 34"><rect x="3" y="7" width="28" height="20"/><path d="M3 7 L17 19 L31 7 M3 27 L13 16 M31 27 L21 16"/></symbol>
    <symbol id="ring" viewBox="0 0 28 28"><circle cx="14" cy="14" r="12" fill="none" stroke="#163f5a" stroke-width="2"/></symbol>
    <symbol id="ringtick" viewBox="0 0 28 28"><path d="M24 8 A12 12 0 1 0 26 14" fill="none" stroke="#163f5a" stroke-width="2"/><polyline points="8,14 13,19 25,6" fill="none" stroke="#163f5a" stroke-width="2.2"/></symbol>
  </defs>
</svg>

<div class="board">

  <!-- General -->
  <section class="phone" style="left:268px;top:119px">
    <svg class="back"><use href="#backarrow"/></svg>
    <h1 class="title">Development Overview</h1>
    <div class="tabs"><span class="tab active">General</span><span class="tab">Compliance<i class="dot"></i></span><span class="tab">Insurances</span><span class="tab">Service Charge</span><span class="tab">Cosec</span></div>
    <div class="card"></div>
    <div class="label" style="top:141px">Handover Date</div>
    <div class="field soft" style="top:168px">12 January 2023<svg width="20" height="20"><use href="#chev"/></svg></div>
    <div class="label" style="top:226px">Units</div>
    <div class="field soft" style="top:252px">85<svg width="20" height="20"><use href="#chev"/></svg></div>
    <div class="label" style="top:309px">Address</div>
    <div class="field soft tall" style="top:336px">24 Alder Grove Road,<br>London, N4 2QT<svg width="20" height="20"><use href="#chev"/></svg></div>
    <div class="label" style="top:411px">Section 20 Limit</div>
    <div class="field soft" style="top:439px">£20<svg width="20" height="20"><use href="#chev"/></svg></div>
    <div class="btn">Next</div>
    <nav class="nav"><div class="nav-item active"><svg><use href="#i-home"/></svg>Home</div><div class="nav-item"><svg><use href="#i-overview"/></svg>Overview</div><div class="nav-item"><svg><use href="#i-fin"/></svg>Finances</div><div class="nav-item"><svg><use href="#i-msg"/></svg>Messages</div></nav>
  </section>

  <!-- Compliance -->
  <section class="phone" style="left:669px;top:119px">
    <svg class="back"><use href="#backarrow"/></svg>
    <h1 class="title">Development Overview</h1>
    <div class="tabs"><span class="tab">General</span><span class="tab active">Compliance<i class="dot"></i></span><span class="tab">Insurances</span><span class="tab">Service Charge</span><span class="tab">Cosec</span></div>
    <div class="card"></div>
    <div class="label" style="top:142px">Asbestos</div>
    <div class="field" style="top:168px">NA<svg width="20" height="20"><use href="#chev"/></svg></div>
    <div class="label" style="top:226px">EICR <span class="flag hint">?</span></div>
    <div class="field" style="top:252px">-<svg width="20" height="20"><use href="#chev"/></svg></div>
    <div class="label" style="top:310px">Drains <span class="flag alert">!</span></div>
    <div class="field" style="top:338px">Overdue 10 December 2023<svg width="20" height="20"><use href="#chev"/></svg></div>
    <div class="label" style="top:393px">Gutters <span class="flag hint">?</span></div>
    <div class="field" style="top:421px">-<svg width="20" height="20"><use href="#chev"/></svg></div>
    <div class="label" style="top:478px">Dry Riser <span class="flag hint">?</span></div>
    <div class="field" style="top:505px">-<svg width="20" height="20"><use href="#chev"/></svg></div>
    <div class="btn">Next</div>
    <nav class="nav"><div class="nav-item active"><svg><use href="#i-home"/></svg>Home</div><div class="nav-item"><svg><use href="#i-overview"/></svg>Overview</div><div class="nav-item"><svg><use href="#i-fin"/></svg>Finances</div><div class="nav-item"><svg><use href="#i-msg"/></svg>Messages</div></nav>
  </section>

  <!-- Insurances -->
  <section class="phone" style="left:1070px;top:119px">
    <svg class="back"><use href="#backarrow"/></svg>
    <h1 class="title">Development Overview</h1>
    <div class="tabs"><span class="tab">General</span><span class="tab">Compliance<i class="dot"></i></span><span class="tab active">Insurances</span><span class="tab">Service Charge</span><span class="tab">Cosec</span></div>
    <div class="card"></div>
    <div class="notes">NA<span>leave it blank if none</span></div>
    <div class="links" style="top:262px"><a>Terrorism</a> <a>Buildings</a> <a>Engineering</a></div>
    <div class="links" style="top:284px"><a>D &amp; O</a> <a>Reinstatemen</a></div>
    <div class="btn">Next</div>
    <nav class="nav"><div class="nav-item active"><svg><use href="#i-home"/></svg>Home</div><div class="nav-item"><svg><use href="#i-overview"/></svg>Overview</div><div class="nav-item"><svg><use href="#i-fin"/></svg>Finances</div><div class="nav-item"><svg><use href="#i-msg"/></svg>Messages</div></nav>
  </section>

  <!-- Service Charge -->
  <section class="phone" style="left:1471px;top:119px">
    <svg class="back"><use href="#backarrow"/></svg>
    <h1 class="title">Development Overview</h1>
    <div class="tabs"><span class="tab">General</span><span class="tab">Compliance<i class="dot"></i></span><span class="tab">Insurances</span><span class="tab active">Service Charge</span><span class="tab">Cosec</span></div>
    <div class="card"></div>
    <div class="label" style="top:142px">Year End</div>
    <div class="field" style="top:168px">12/12/2024<svg width="20" height="20"><use href="#chev"/></svg></div>
    <div class="label" style="top:226px">Demand Dates</div>
    <div class="field" style="top:253px">NA<svg width="20" height="20"><use href="#chev"/></svg></div>
    <div class="btn">Next</div>
    <nav class="nav"><div class="nav-item active"><svg><use href="#i-home"/></svg>Home</div><div class="nav-item"><svg><use href="#i-overview"/></svg>Overview</div><div class="nav-item"><svg><use href="#i-fin"/></svg>Finances</div><div class="nav-item"><svg><use href="#i-msg"/></svg>Messages</div></nav>
  </section>

  <!-- Cosec -->
  <section class="phone" style="left:268px;top:913px">
    <svg class="back"><use href="#backarrow"/></svg>
    <h1 class="title">Development Overview</h1>
    <div class="tabs"><span class="tab">General</span><span class="tab">Compliance<i class="dot"></i></span><span class="tab">Insurances</span><span class="tab">Service Charge</span><span class="tab active">Cosec</span></div>
    <div class="card"></div>
    <div class="center-label" style="top:142px">Are We Responsible?</div>
    <div class="choice" style="left:52px">Yes</div>
    <div class="choice" style="left:170px">No</div>
    <div class="btn">Continue</div>
    <nav class="nav"><div class="nav-item active"><svg><use href="#i-home"/></svg>Home</div><div class="nav-item"><svg><use href="#i-overview"/></svg>Overview</div><div class="nav-item"><svg><use href="#i-fin"/></svg>Finances</div><div class="nav-item"><svg><use href="#i-msg"/></svg>Messages</div></nav>
  </section>

  <!-- Finances -->
  <section class="phone" style="left:669px;top:913px">
    <svg class="back"><use href="#backarrow"/></svg>
    <h1 class="title">Finances</h1>
    <div class="tabs"><span class="tab active">Subaccount</span><span class="tab">Payment Provider<i class="dot ok"></i></span></div>
    <div class="card"></div>
    <div class="center-label" style="top:142px">Receivable</div>
    <div class="money" style="top:168px"><b>£7,268.22</b><small>5 Bill(s)</small><small>Arrears Total</small><svg width="20" height="20"><use href="#chev"/></svg></div>
    <div class="money" style="top:283px"><b>£7,268.22</b><small>5 Receipt(s)</small><small>Unallocated Total</small><svg width="20" height="20"><use href="#chev"/></svg></div>
    <div class="center-label" style="top:413px">Payable</div>
    <div class="money pay" style="top:440px"><b>£4,268.78</b><small>5 Invoice(s) Total</small><svg width="20" height="20"><use href="#chev"/></svg></div>
    <nav class="nav"><div class="nav-item"><svg><use href="#i-home"/></svg>Home</div><div class="nav-item"><svg><use href="#i-overview"/></svg>Overview</div><div class="nav-item active"><svg><use href="#i-fin"/></svg>Finances</div><div class="nav-item"><svg><use href="#i-msg"/></svg>Messages</div></nav>
  </section>

  <!-- Legionellas -->
  <section class="phone" style="left:1070px;top:913px">
    <svg class="back"><use href="#backarrow"/></svg>
    <h1 class="title">Legionellas</h1>
    <div class="card plain"></div>
    <div class="label" style="top:142px">Is it required?</div>
    <div class="option" style="top:172px">No<svg width="28" height="28"><use href="#ring"/></svg></div>
    <div class="option" style="top:222px">Yes, but I do not have a file to upload<svg width="28" height="28"><use href="#ring"/></svg></div>
    <div class="option" style="top:273px">Yes, and I have a file to upload<svg width="28" height="28"><use href="#ringtick"/></svg></div>
    <div class="btn">Next</div>
    <nav class="nav"><div class="nav-item active"><svg><use href="#i-home"/></svg>Home</div><div class="nav-item"><svg><use href="#i-overview"/></svg>Overview</div><div class="nav-item"><svg><use href="#i-fin"/></svg>Finances</div><div class="nav-item"><svg><use href="#i-msg"/></svg>Messages</div></nav>
  </section>

</div>
</body>
</html>
```